Beekeeper needs box/label design for honey/CBD and other honey-related products

We need a box (or label) design for a beekeeping company in Virginia called Tamsin Hollow Farm. Our products will include honey mixed with CBD oil and other essential oils (vanilla, lavender, etc).The box design should be scalable to include several different honey/oil products. We would like to incorporate our current farm logo into the design. Here is a link to a honey producing company with a series of products using their honey mixed with certain oils. It's a good reference of what type box/label design we would like (https://corbinandlyle.co/pages/honey).

Target Market(s)

Retail stores and consumers

Requirements
Must have
• Tamsin Hollow Farm name and logo

```html
<!DOCTYPE html>
<html lang="en">
<head>
<meta charset="utf-8">
<title>Tamsin Hollow Farm – Honey with Essential Oils Labels</title>
<link href="https://fonts.googleapis.com/css2?family=Cormorant+Garamond:ital,wght@0,300;0,400;0,600;1,500&family=Playfair+Display:wght@800&family=Pinyon+Script&family=Playball&family=Lato:wght@400&display=swap" rel="stylesheet">
<style>
  :root {
    --page: #ffffff;
    --olive: #9bab3e;
    --ink: #2b2b2b;
    --green: #4b7350;
    --purple: #6a4e7e;
    --brown: #55392b;
    --faint-green: #e6e8e4;
    --faint-purple: #e7e2ec;
    --faint-brown: #ede5e2;
  }
  * { box-sizing: border-box; margin: 0; padding: 0; }
  html, body {
    width: 1200px; height: 1033px; overflow: hidden;
    background: var(--page);
  }
  .label-row {
    position: absolute; top: 285px; left: 30px;
    display: flex; gap: 30px;
  }
  .label {
    position: relative; width: 360px; height: 462px;
    background: #fff; overflow: hidden;
    box-shadow: 0 0 0 1px #f1f1f1;
  }
  .label--cbd { --accent: var(--green); --faint: var(--faint-green); --flavor-size: 86px; --flavor-left: 4px; --flavor-bottom: 166px; }
  .label--lavender { --accent: var(--purple); --faint: var(--faint-purple); --flavor-size: 64px; --flavor-left: 6px; --flavor-bottom: 100px; }
  .label--vanilla { --accent: var(--brown); --faint: var(--faint-brown); --flavor-size: 86px; --flavor-left: 4px; --flavor-bottom: 90px; }

  .band {
    position: absolute; left: 0; right: 0; height: 27px;
    background: var(--accent);
  }
  .band::after {
    content: ""; position: absolute; left: 0; right: 0; height: 2px; background: #fff;
  }
  .band--top { top: 0; }
  .band--top::after { top: 20px; }
  .band--bottom { bottom: 0; }
  .band--bottom::after { top: 5px; }

  .flavor-watermark {
    position: absolute; left: var(--flavor-left); bottom: var(--flavor-bottom);
    writing-mode: vertical-rl; transform: rotate(180deg);
    font: 300 var(--flavor-size)/1 "Cormorant Garamond", serif;
    color: var(--faint); letter-spacing: 1px;
  }

  .tagline {
    position: absolute; top: 42px; left: 0; right: 0; text-align: center;
    font: italic 500 19px/1 "Cormorant Garamond", serif; color: var(--ink);
  }
  .tagline span { display: inline-block; padding: 0 2px 5px; border-bottom: 3px double var(--accent); }

  .farm-mark {
    position: absolute; top: 86px; left: 0; right: 0;
    display: flex; flex-direction: column; align-items: center; gap: 10px;
  }
  .farm-mark__square { width: 54px; height: 54px; background: var(--olive); }
  .farm-mark__name {
    font: 600 17px/1 "Cormorant Garamond", serif; color: #8a7f3d;
    letter-spacing: 1.5px; text-transform: uppercase;
  }

  .product-name {
    position: absolute; top: 204px; left: 0; right: 0; height: 140px; text-align: center;
  }
  .product-name__flavor {
    display: block; font: 800 50px/1 "Playfair Display", serif; color: var(--accent);
  }
  .product-name__oil {
    position: absolute; top: 26px; left: 0; right: 0; text-align: center;
    font: 44px/1 "Playball", cursive; color: var(--olive); transform: rotate(-8deg);
  }
  .product-name__honey {
    position: absolute; top: 56px; left: 0; right: 0; text-align: center;
    font: 64px/1 "Pinyon Script", cursive; color: var(--accent); font-weight: 400;
  }

  .net-weight {
    position: absolute; top: 231px; right: 14px; height: 180px;
    writing-mode: vertical-rl; transform: rotate(180deg);
    display: flex; align-items: center; gap: 12px;
    font: 400 11.5px/1 "Lato", sans-serif; color: var(--ink);
  }
  .net-weight__dots { display: flex; gap: 6px; }
  .net-weight__dots i { display: block; width: 6px; height: 6px; border-radius: 50%; background: var(--accent); }

  .description {
    position: absolute; top: 380px; left: 20px; width: 300px;
    font: 400 10.6px/1.08 "Lato", sans-serif; color: var(--ink);
  }
</style>
</head>
<body>
<main class="label-row">

  <article class="label label--cbd">
    <div class="band band--top"></div>
    <div class="flavor-watermark">CBD</div>
    <p class="tagline"><span>HONEY &nbsp;with ESSENTIAL OILS</span></p>
    <div class="farm-mark"><div class="farm-mark__square"></div><p class="farm-mark__name">Tamsin Hollow Farm</p></div>
    <h2 class="product-name">
      <span class="product-name__flavor">CBD</span>
      <span class="product-name__oil">oil</span>
      <span class="product-name__honey">Honey</span>
    </h2>
    <div class="net-weight">
      <span class="net-weight__dots"><i></i><i></i><i></i></span>
      <span>Net weight 750 g</span>
      <span class="net-weight__dots"><i></i><i></i><i></i></span>
    </div>
    <p class="description">Lorem ipsum dolor sit amet, consectetuer adipiscing elit. Aenean commodo ligula eget dolor. Aenean massa. Cum sociis natoque penatibus et magnis dis parturient montes, nascetur ridiculus mus.</p>
    <div class="band band--bottom"></div>
  </article>

  <article class="label label--lavender">
    <div class="band band--top"></div>
    <div class="flavor-watermark">LAVENDER</div>
    <p class="tagline"><span>HONEY &nbsp;with ESSENTIAL OILS</span></p>
    <div class="farm-mark"><div class="farm-mark__square"></div><p class="farm-mark__name">Tamsin Hollow Farm</p></div>
    <h2 class="product-name">
      <span class="product-name__flavor">LAVENDE</span>
      <span class="product-name__oil">oil</span>
      <span class="product-name__honey">Honey</span>
    </h2>
    <div class="net-weight">
      <span class="net-weight__dots"><i></i><i></i><i></i></span>
      <span>Net weight 750 g</span>
      <span class="net-weight__dots"><i></i><i></i><i></i></span>
    </div>
    <p class="description">Lorem ipsum dolor sit amet, consectetuer adipiscing elit. Aenean commodo ligula eget dolor. Aenean massa. Cum sociis natoque penatibus et magnis dis parturient montes, nascetur ridiculus mus.</p>
    <div class="band band--bottom"></div>
  </article>

  <article class="label label--vanilla">
    <div class="band band--top"></div>
    <div class="flavor-watermark">VANILLA</div>
    <p class="tagline"><span>HONEY &nbsp;with ESSENTIAL OILS</span></p>
    <div class="farm-mark"><div class="farm-mark__square"></div><p class="farm-mark__name">Tamsin Hollow Farm</p></div>
    <h2 class="product-name">
      <span class="product-name__flavor">VANILLA</span>
      <span class="product-name__oil">oil</span>
      <span class="product-name__honey">Honey</span>
    </h2>
    <div class="net-weight">
      <span class="net-weight__dots"><i></i><i></i><i></i></span>
      <span>Net weight 750 g</span>
      <span class="net-weight__dots"><i></i><i></i><i></i></span>
    </div>
    <p class="description">Lorem ipsum dolor sit amet, consectetuer adipiscing elit. Aenean commodo ligula eget dolor. Aenean massa. Cum sociis natoque penatibus et magnis dis parturient montes, nascetur ridiculus mus.</p>
    <div class="band band--bottom"></div>
  </article>

</main>
</body>
</html>
```